Local Flower Farm Needs Business Card Design

I need business cards designed for a flower farm based in Eudora, Kansas.
Business Info:
We are a local cut flower farm located in Eudora, Kansas, founded by Darla Whitcombe. What started as a passion for agriculture and search for more joy in daily life has blossomed into a small business dedicated to providing the community with beautiful, fresh, and sustainable flowers. We specialize in local, seasonal blooms, ensuring that every petal reflects the care and dedication we pour into our craft. Our mission is to deliver the highest quality flowers directly to our customers through local farmers markets and to florists who share our commitment to sustainability. Join us in celebrating the beauty of nature, one bloom at a time!
Contact Details:
Darla Whitcombe
Owner
Phone 913-555-0148
Facebook: Rosalind Pike Gardens
Instagram: @RosalindPikeGardens
Website: RosalindPikeGardens.example
Target Market(s)
Wholesale to Florists and Direct to Consumer via Farmers Market
Industry/Entity Type
Florist, Farm
Contact Information for Business Card
Name, Contact Info, Logo
Look and feel
Each slider illustrates characteristics of the customer's brand and the style your logo design should communicate.

```html
<!DOCTYPE html>
<html lang="en">
<head>
<meta charset="utf-8">
<title>Rosalind Pike Gardens — Business Card</title>
<link href="https://fonts.googleapis.com/css2?family=Tinos:wght@400;700&display=swap" rel="stylesheet">
<style>
  :root {
    --ink: #0b2730;
    --paper: #ffffff;
    --backdrop: #e3e7e9;
    --black: #111111;
  }
  * { margin: 0; padding: 0; box-sizing: border-box; }
  html, body { width: 1200px; height: 960px; overflow: hidden; }
  body { background: var(--backdrop); font-family: "Tinos", "Times New Roman", serif; position: relative; }

  .card {
    position: absolute;
    top: 106px;
    width: 429px;
    height: 749px;
    border-radius: 26px;
    overflow: hidden;
  }
  .card--front { left: 142px; background: var(--ink); }
  .card--back { left: 630px; background: var(--paper); }

  .brand-mark {
    position: absolute;
    border-radius: 50%;
    display: flex;
    align-items: center;
    justify-content: center;
    text-align: center;
    font-family: "Tinos", "Times New Roman", serif;
    font-weight: 400;
    text-transform: uppercase;
    letter-spacing: 0.12em;
  }
  .card--front .brand-mark {
    left: 71px; top: 231px; width: 286px; height: 286px;
    border: 1px solid var(--paper);
    color: var(--paper);
    font-size: 27px; line-height: 1.35;
  }
  .card--back .brand-mark {
    left: 116px; top: 29px; width: 198px; height: 198px;
    border: 1px solid var(--ink);
    color: var(--ink);
    font-size: 19px; line-height: 1.35;
  }

  .owner-name {
    position: absolute; left: 0; right: 0; top: 440px;
    text-align: center;
    font-weight: 700; font-size: 34px; letter-spacing: 0.01em;
    color: var(--black);
  }
  .owner-role {
    position: absolute; left: 0; right: 0; top: 482px;
    text-align: center;
    font-size: 18px; color: var(--black);
  }

  .contact-table { position: absolute; left: 0; right: 0; top: 518px; bottom: 0; }
  .contact-table .divider {
    position: absolute; left: 73px; top: 0; bottom: 0;
    width: 1.5px; background: var(--ink);
  }
  .contact-row {
    position: absolute; left: 0; right: 0; height: 45px;
    border-top: 1.5px solid var(--ink);
    display: flex; align-items: center;
  }
  .contact-row.last { border-bottom: 1.5px solid var(--ink); }
  .contact-icon { width: 73px; display: flex; justify-content: center; }
  .contact-text { padding-left: 21px; font-size: 19px; color: var(--black); letter-spacing: 0.01em; }
</style>
</head>
<body>

<section class="card card--front">
  <div class="brand-mark">Rosalind<br>Pike<br>Gardens</div>
</section>

<section class="card card--back">
  <div class="brand-mark">Rosalind<br>Pike<br>Gardens</div>

  <h1 class="owner-name">Darla Whitcombe</h1>
  <p class="owner-role">Owner</p>

  <div class="contact-table">
    <div class="divider"></div>

    <div class="contact-row" style="top:26px">
      <span class="contact-icon">
        <svg width="24" height="24" viewBox="0 0 24 24" aria-hidden="true">
          <path fill="var(--ink)" d="M6.6 10.8a15 15 0 0 0 6.6 6.6l2.2-2.2a1 1 0 0 1 1-.25 11.4 11.4 0 0 0 3.6.57 1 1 0 0 1 1 1V20a1 1 0 0 1-1 1A17 17 0 0 1 3 4a1 1 0 0 1 1-1h3.5a1 1 0 0 1 1 1c0 1.25.2 2.45.57 3.6a1 1 0 0 1-.25 1z"/>
          <path fill="none" stroke="var(--ink)" stroke-width="1.6" stroke-linecap="round" d="M14 7a3 3 0 0 1 3 3M14 3.5a6.5 6.5 0 0 1 6.5 6.5"/>
        </svg>
      </span>
      <span class="contact-text">913-555-0148</span>
    </div>

    <div class="contact-row" style="top:71px">
      <span class="contact-icon">
        <svg width="28" height="28" viewBox="0 0 28 28" aria-hidden="true"><circle cx="14" cy="14" r="13" fill="var(--ink)"/></svg>
      </span>
      <span class="contact-text">Rosalind Pike Gardens</span>
    </div>

    <div class="contact-row" style="top:115px">
      <span class="contact-icon">
        <svg width="28" height="28" viewBox="0 0 28 28" aria-hidden="true"><rect x="2" y="2" width="24" height="24" rx="6" fill="none" stroke="var(--ink)" stroke-width="3"/></svg>
      </span>
      <span class="contact-text">@RosalindPikeGardens</span>
    </div>

    <div class="contact-row last" style="top:160px">
      <span class="contact-icon">
        <svg width="26" height="26" viewBox="0 0 26 26" aria-hidden="true">
          <circle cx="13" cy="13" r="11.5" fill="none" stroke="var(--ink)" stroke-width="1.8"/>
          <ellipse cx="13" cy="13" rx="5" ry="11.5" fill="none" stroke="var(--ink)" stroke-width="1.4"/>
          <path d="M1.5 13h23M3.5 7.5h19M3.5 18.5h19" stroke="var(--ink)" stroke-width="1.4"/>
        </svg>
      </span>
      <span class="contact-text">RosalindPikeGardens.example</span>
    </div>
  </div>
</section>

</body>
</html>
```